Brightbay Business Card Design

Our company is called Brightbay. We manufacture confectionary snacks & frozen novelties. Our initial product portfolio includes frozen ice lollies/popsicles & stick ice cream bars.

We require a business card design.

Please use the attached Logo.

Please use an orange, brown, yellow colour code. You may choose any combination of the 3 or include all three. The logo however must remain orange.

Target Market(s)

Business card will be targeted at distributors of our products such as supermarket procurement managers, convenience store owners, wholesale distributors and merchandising agents.

Industry/Entity Type

Business

Requirements
Must have
• Calvin Obeng_Director/ P.O.Box Dunmore 5172, Accra, Ghana / m: 00233(0)507318924/ e: calvin.obeng@mailvora.co.uk

```html
<!DOCTYPE html>
<html lang="en">
<head>
<meta charset="utf-8">
<title>Brightbay Business Card</title>
<link rel="stylesheet" href="https://fonts.googleapis.com/css2?family=Libre+Baskerville:wght@400;700&display=swap">
<style>
  :root {
    --orange-light: #f7a044;
    --orange: #f26f2a;
    --orange-deep: #ee4f23;
    --yellow: #fbe13a;
    --yellow-pale: #f6ee84;
    --ink: #333333;
    --paper: #ffffff;
    --backdrop: #d9d9d9;
  }
  * { margin: 0; padding: 0; box-sizing: border-box; }
  html, body {
    width: 1200px;
    height: 985px;
    overflow: hidden;
    background: var(--backdrop);
  }
  .canvas {
    position: relative;
    width: 1200px;
    height: 985px;
  }
  .business-card {
    position: absolute;
    left: 150px;
    top: 232px;
    width: 900px;
    height: 520px;
    border-radius: 26px;
    overflow: hidden;
    background: var(--paper);
    box-shadow: 0 14px 30px rgba(0,0,0,0.18);
    font-family: "Libre Baskerville", Georgia, serif;
  }
  .card-art {
    position: absolute;
    inset: 0;
  }
  .holder {
    position: absolute;
    left: 56px;
    top: 30px;
    color: var(--paper);
  }
  .holder-name {
    font-size: 30px;
    font-weight: 400;
    line-height: 1.1;
  }
  .holder-title {
    font-size: 20px;
    line-height: 1.2;
  }
  .contact {
    position: absolute;
    left: 56px;
    top: 150px;
    font-size: 19px;
    line-height: 1.35;
  }
  .contact-line {
    display: flex;
    align-items: center;
    gap: 8px;
    color: var(--ink);
  }
  .contact-icon {
    width: 20px;
    height: 16px;
    flex: none;
  }
  .address {
    margin-top: 8px;
    color: var(--orange);
  }
  .brand {
    position: absolute;
    left: 560px;
    top: 228px;
    display: flex;
    align-items: center;
    gap: 14px;
  }
  .brand-dot {
    width: 40px;
    height: 40px;
    border-radius: 50%;
    background: var(--orange);
  }
  .brand-name {
    font-size: 50px;
    font-weight: 700;
    color: var(--orange);
    letter-spacing: -0.5px;
  }
</style>
</head>
<body>
<main class="canvas">
  <article class="business-card">
    <svg class="card-art" viewBox="0 0 900 520" width="900" height="520" aria-hidden="true">
      <defs>
        <linearGradient id="band-top" x1="0" y1="0" x2="1" y2="0.4">
          <stop offset="0" stop-color="var(--orange-light)"/>
          <stop offset="0.6" stop-color="var(--orange)"/>
          <stop offset="1" stop-color="var(--orange-deep)"/>
        </linearGradient>
        <linearGradient id="band-bottom" x1="0" y1="0" x2="1" y2="0">
          <stop offset="0" stop-color="var(--orange-light)"/>
          <stop offset="0.5" stop-color="var(--orange)"/>
          <stop offset="1" stop-color="var(--orange-deep)"/>
        </linearGradient>
      </defs>
      <!-- top band with trailing yellow stripes -->
      <path d="M0,116 C220,108 420,150 600,210 C730,254 820,290 900,330 V0 H0 Z" fill="var(--yellow-pale)"/>
      <path d="M0,104 C220,96 420,134 600,192 C730,236 820,266 900,300 V0 H0 Z" fill="var(--paper)"/>
      <path d="M0,98 C220,88 420,124 600,180 C730,222 820,250 900,282 V0 H0 Z" fill="var(--yellow)"/>
      <path d="M0,90 C220,78 420,112 600,166 C730,206 820,232 900,262 V0 H0 Z" fill="url(#band-top)"/>
      <!-- bottom band with yellow stripes above -->
      <path d="M250,520 C420,468 600,450 720,420 C810,398 870,378 900,362 V520 Z" fill="var(--yellow-pale)"/>
      <path d="M270,520 C430,476 600,462 720,434 C810,412 870,392 900,378 V520 Z" fill="var(--paper)"/>
      <path d="M285,520 C440,482 610,470 725,444 C812,424 870,404 900,390 V520 Z" fill="var(--yellow)"/>
      <path d="M305,520 C450,490 615,480 730,456 C815,438 870,418 900,404 V520 Z" fill="url(#band-bottom)"/>
    </svg>

    <header class="holder">
      <h1 class="holder-name">Calvin Obeng</h1>
      <p class="holder-title">Director</p>
    </header>

    <section class="contact">
      <p class="contact-line">
        <svg class="contact-icon" viewBox="0 0 20 16" aria-label="Phone" role="img">
          <rect x="1" y="2" width="18" height="13" rx="3" fill="var(--orange)"/>
          <path d="M3,5 C3,1 17,1 17,5 L14,6 L13,4 H7 L6,6 Z" fill="var(--paper)"/>
          <circle cx="10" cy="10" r="3" fill="var(--paper)"/>
        </svg>
        00233(0)507318924
      </p>
      <p class="contact-line">
        <svg class="contact-icon" viewBox="0 0 20 16" aria-label="Email" role="img">
          <rect x="1" y="2" width="18" height="13" rx="1.5" fill="var(--orange)"/>
          <path d="M2,3 L10,9.5 L18,3" fill="none" stroke="var(--paper)" stroke-width="1.6"/>
        </svg>
        calvin.obeng@mailvora.co.uk
      </p>
      <p class="address">P.O.Box Dunmore 5172,<br>Accra, Ghana</p>
    </section>

    <div class="brand">
      <span class="brand-dot"></span>
      <span class="brand-name">Brightbay</span>
    </div>
  </article>
</main>
</body>
</html>
```